Business card design for global fintech startup

Veltrix is a modern payments platform for the global insurance industry, serving international health, life, and travel insurers, MGAs, brokers, and partners.

We need a professional, premium business card for use at insurance conferences and executive meetings. The goal is to create a card that feels trustworthy, modern, and high-quality, while still being distinctive and memorable in a stack of business cards.

Target audience:
Senior insurance executives (VP, C-suite).

Design goals:
Clear, professional, and credible
Modern but not trendy
Premium and well-structured
Easy to read and practical for networking

Brand direction:
Brand-first (company over individual)
Follow existing brand guidelines where possible
Clean layout, strong hierarchy, excellent readability

Must include:
Name
Title
Company name (Veltrix)
Logo
Email
Phone/Whatsapp
Website (www.withveltrix.example)
Tagline - Secure Flow For Insurers

Materials & finish:
Open to designer recommendations for premium look and feel.

Please avoid:
Flashy or trendy startup styles
Generic insurance icons or clichés
Cluttered layouts or hard-to-read text

Deliverables:
Front and back business card, print-ready files.

Target Market(s)

Global Insurance executives

Industry/Entity Type

Fintech, Insurtech, Insurance, Financial Services

Contact Information for Business Card

Name Title Company name (Veltrix) Logo Email Phone/Whatsapp Website (www.withveltrix.example) Tagline - Secure Flow For Insurers

Font styles to use
Other font styles liked:
• See brand guidelines

Requirements
Nice to have
• something that stands out/makes us more memorable while still remaining professional
Should not have
• Please avoid: Flashy or trendy startup styles Generic insurance icons or clichés Cluttered layouts or hard-to-read text

```html
<!DOCTYPE html>
<html lang="en">
<head>
<meta charset="utf-8">
<title>Veltrix Business Card</title>
<link rel="stylesheet" href="https://fonts.googleapis.com/css2?family=Montserrat:wght@700&family=Ubuntu:wght@400;500&display=swap">
<style>
  :root {
    --backdrop: #d1d5d7;
    --card-dark: #1c1c1c;
    --card-light: #ffffff;
    --ink: #1a1a1a;
    --ink-soft: #2a2a2a;
    --white: #ffffff;
    --orange: #f07622;
    --violet: #5c4398;
    --sky: #35b9e6;
    --green: #3dba4e;
  }
  * { margin: 0; padding: 0; box-sizing: border-box; }
  html, body {
    width: 900px; height: 1200px; overflow: hidden;
    background: var(--backdrop);
  }
  .canvas { position: relative; width: 900px; height: 1200px; }

  .card { position: absolute; left: 134px; width: 633px; height: 363px; }
  .card--front { top: 212px; background: var(--card-dark); display: flex; align-items: center; justify-content: center; }
  .card--back { top: 627px; background: var(--card-light); color: var(--ink); }

  .front-brand { display: flex; align-items: center; gap: 26px; }
  .brand-dot { width: 30px; height: 30px; border-radius: 50%; background: var(--orange); }
  .front-wordmark {
    font-family: "Ubuntu", sans-serif; font-weight: 500;
    font-size: 64px; letter-spacing: 0.08em; color: var(--white); line-height: 1;
  }

  .person { position: absolute; left: 52px; top: 54px; }
  .person-name { font-family: "Montserrat", sans-serif; font-weight: 700; font-size: 24px; letter-spacing: 0.02em; line-height: 1; }
  .person-title { font-family: "Ubuntu", sans-serif; font-size: 15px; margin-top: 7px; color: var(--ink-soft); letter-spacing: 0.02em; }

  .address { position: absolute; left: 46px; top: 167px; font-style: normal; font-family: "Ubuntu", sans-serif; font-size: 15px; line-height: 26px; letter-spacing: 0.02em; color: var(--ink-soft); }

  .contacts { position: absolute; left: 50px; top: 234px; list-style: none; font-family: "Ubuntu", sans-serif; font-size: 15px; color: var(--ink-soft); }
  .contact { display: flex; align-items: center; height: 27px; gap: 9px; letter-spacing: 0.03em; }
  .contact svg { width: 17px; height: 17px; flex: none; }
  .contact--phone { letter-spacing: 0.18em; }
  .chat-dot { width: 17px; height: 17px; border-radius: 50%; background: var(--green); margin-left: -4px; }

  .brand-block { position: absolute; left: 320px; top: 60px; width: 275px; height: 245px; display: flex; flex-direction: column; align-items: center; justify-content: flex-end; }
  .back-wordmark { font-family: "Ubuntu", sans-serif; font-weight: 500; font-size: 54px; letter-spacing: 0.08em; color: var(--ink); line-height: 1; margin-bottom: 58px; }
  .tagline { font-family: "Ubuntu", sans-serif; font-weight: 500; font-size: 17px; letter-spacing: 0.07em; color: var(--ink); white-space: nowrap; }
</style>
</head>
<body>
<main class="canvas">
  <section class="card card--front" aria-label="Card front">
    <div class="front-brand">
      <span class="brand-dot"></span>
      <span class="front-wordmark">VELTRIX</span>
    </div>
  </section>

  <section class="card card--back" aria-label="Card back">
    <div class="person">
      <h1 class="person-name">Daniel Rourke</h1>
      <p class="person-title">Co-Founder &amp; President</p>
    </div>

    <address class="address">
      4200 Harbor Park Dr 2nd floor<br>
      Austin TX 78701
    </address>

    <ul class="contacts">
      <li class="contact contact--phone">
        <svg viewBox="0 0 20 20" aria-hidden="true"><path d="M5 2 L8 6 L6.5 8 Q8 11.5 12 13.5 L14 12 L18 15 L16 18 Q9 18 5 13 Q2 9 3 4 Z" fill="var(--orange)"/></svg>
        (555) 014-2370 <span class="chat-dot"></span>
      </li>
      <li class="contact">
        <svg viewBox="0 0 20 20" aria-hidden="true"><rect x="1" y="4" width="18" height="13" fill="var(--violet)"/><path d="M1 4 L10 11 L19 4" fill="none" stroke="var(--white)" stroke-width="1.6"/></svg>
        info@withveltrix.example
      </li>
      <li class="contact">
        <svg viewBox="0 0 20 20" aria-hidden="true"><g fill="none" stroke="var(--sky)" stroke-width="1.5"><circle cx="10" cy="10" r="8"/><ellipse cx="10" cy="10" rx="3.5" ry="8"/><path d="M2 10 H18 M3.5 6 H16.5 M3.5 14 H16.5"/></g></svg>
        www.withveltrix.example
      </li>
    </ul>

    <div class="brand-block">
      <span class="back-wordmark">Veltrix</span>
      <p class="tagline">Secure Flow For Insurers</p>
    </div>
  </section>
</main>
</body>
</html>
```